Powerpoint design for Halvora Trade Allies

We would like to have a Power point template/design with flexibilities and good opportunities to do changes.
• Be able to change in image background
• Themes are HTA colors and complementary colors. Please come with suggestions.
• Alternate white and blue background
• Standard functions and opportunities within Powerpoint should be able to be used or be accessible.
• Feel free to change/alter the logo for example remove or separate the text in the logo ("Halvora Trade Allies" ) and the tagline ("we create competitiveness")
• www.halvoratradeallies.se

```html
<!DOCTYPE html>
<html lang="en">
<head>
<meta charset="utf-8">
<title>Halvora Trade Allies – Presentation Template</title>
<link href="https://fonts.googleapis.com/css2?family=Montserrat:wght@400;500;600;700&display=swap" rel="stylesheet">
<style>
:root{
  --blue:#0b4a93;
  --blue-dark:#07346b;
  --orange:#f08a1e;
  --ink:#1d1d1f;
  --grey-text:#555;
  --sheet:#b9b9bd;
  --bar-dark:#3a3a3c;
  --white:#fff;
}
*{box-sizing:border-box;margin:0;padding:0}
html,body{width:1200px;height:2875px;overflow:hidden}
body{background:var(--sheet);font-family:"Montserrat",sans-serif;color:var(--ink);position:relative}
.hero{position:absolute;left:0;top:0;width:1200px;height:792px;background:linear-gradient(180deg,#dfe2ea 0%,#cdd2dc 55%,#d9cfc6 100%)}
.hero-brand{position:absolute;left:840px;top:140px;text-align:center;color:var(--blue)}
.hero-brand .name{font-size:25px;font-weight:500}
.hero-brand .tagline{font-size:12.5px;letter-spacing:2px;margin-top:4px}
.hero .slide{left:150px;top:230px;box-shadow:0 20px 40px rgba(0,0,0,.25)}

.slide{position:absolute;width:563px;height:316px;overflow:hidden;background:var(--white)}
.photo{position:absolute}
.abs{position:absolute}
.brand-word{position:absolute;font-weight:600;color:var(--blue);font-size:11px;white-space:nowrap}
.brand-word.light{color:var(--white)}
.copyright{position:absolute;left:52px;top:274px;font-size:5.5px;color:#aaa}
.arc{position:absolute;width:130px;height:130px;border-radius:50%;background:rgba(255,255,255,.25)}

.t-small{font-size:19px;font-weight:500}
.t-big{font-size:30px;font-weight:700;line-height:1.05}
.t-sub{font-size:16.5px;font-weight:400;line-height:1.1}
.t-date{font-size:8.5px;font-weight:500}

.footer .lead{position:absolute;left:0;top:290px;width:28px;height:7px;background:var(--orange)}
.footer .mark{position:absolute;left:31px;top:282px;font-size:18px;font-weight:700;color:var(--blue)}
.footer .line{position:absolute;left:82px;top:290px;width:460px;height:7px;background:var(--blue)}
.footer .page{position:absolute;left:536px;top:286px;width:15px;height:15px;border-radius:50%;background:var(--orange);color:#fff;font-size:7px;text-align:center;line-height:15px}

.slide-title{position:absolute;left:0;width:100%;text-align:center;font-size:22px;font-weight:700}
.slide-title .plain{font-weight:400;color:var(--ink)}
.blue{color:var(--blue)}
.orange{color:var(--orange)}

.focus h2{position:absolute;font-size:22px;font-weight:700;color:var(--blue)}
.focus h3{position:absolute;font-size:17px;font-weight:400;color:var(--orange);line-height:1.05}
.focus ul{position:absolute;list-style:none;font-size:10.5px;line-height:1.6}
.focus li{padding-left:14px;position:relative}
.focus li::before{content:"";position:absolute;left:1px;top:6px;width:4px;height:4px;background:var(--orange);border-radius:1px}

.step{position:absolute;top:118px;width:120px;text-align:center}
.step .dot{width:54px;height:54px;border-radius:50%;margin:0 auto;border:3px solid #fff;display:flex;align-items:center;justify-content:center;box-shadow:0 1px 3px rgba(0,0,0,.2)}
.step .label{font-size:9px;margin-top:9px;line-height:1.1}
.step .desc{font-size:6.4px;margin-top:9px;line-height:1.2;color:#333}

.legend{position:absolute;left:340px;width:190px}
.legend .item{margin-bottom:20px;position:relative;padding-left:20px}
.legend .item i{position:absolute;left:0;top:1px;width:11px;height:11px;border-radius:50%}
.legend b{font-size:10px;font-weight:500;display:block}
.legend p{font-size:6.4px;line-height:1.15;margin-top:4px;color:#333}

table.data{position:absolute;left:40px;top:82px;width:482px;border-collapse:collapse;font-size:9.5px}
table.data th{background:var(--blue);color:#fff;font-weight:500;height:30px;text-align:center;border-right:1px solid #fff}
table.data th:first-child{text-align:left;padding-left:6px}
table.data th.accent{background:var(--orange)}
table.data td{height:31px;text-align:center;border:1px solid #cfd3da;color:#333}
table.data td:first-child{text-align:left;padding-left:6px}

.contact{position:absolute;color:#fff}
.contact .mark{font-size:28px;font-weight:700;color:var(--blue)}
.contact h4{font-size:15px;font-weight:700;margin-top:10px}
.contact .addr{font-size:7.5px;margin-top:6px;line-height:1.2}
.contact .row{display:flex;align-items:center;gap:8px;font-size:8px;margin-top:6px}
.contact svg{width:10px;height:10px}
</style>
</head>
<body>

<section class="hero">
  <div class="hero-brand">
    <div class="name">Halvora Trade Allies</div>
    <div class="tagline">We create competitiveness</div>
  </div>
  <div class="slide title-blue">
    <div class="photo" role="img" aria-label="Photo of a hand touching a tablet with a shopping cart, tinted deep blue" style="left:0;top:0;width:563px;height:237px;background:linear-gradient(110deg,#0b4a93 0%,#0d4c92 45%,#3c6aa3 75%,#2d5c98 100%)"></div>
    <div class="arc" style="left:420px;top:190px"></div>
    <div class="abs" style="left:52px;top:44px;color:#fff">
      <div class="t-small">We Create</div>
      <div class="t-big">Digital Competitiveness</div>
      <div class="t-sub" style="margin-top:14px">Subtitle of Presentation<br>Goes Here!</div>
      <div class="t-date" style="margin-top:26px">Friday, April 16, 2021</div>
    </div>
    <div class="copyright">© Copyright Halvora Trade Allies</div>
    <div class="brand-word" style="left:420px;top:270px">Halvora Trade Allies</div>
  </div>
</section>

<!-- Row 1 -->
<div class="slide title-blue" style="left:28px;top:810px">
  <div class="photo" role="img" aria-label="Photo of a hand touching a tablet with a shopping cart, tinted deep blue" style="left:0;top:0;width:563px;height:237px;background:linear-gradient(110deg,#0b4a93 0%,#0d4c92 45%,#3c6aa3 75%,#2d5c98 100%)"></div>
  <div class="arc" style="left:420px;top:190px"></div>
  <div class="abs" style="left:52px;top:44px;color:#fff">
    <div class="t-small">We Create</div>
    <div class="t-big">Digital Competitiveness</div>
    <div class="t-sub" style="margin-top:14px">Subtitle of Presentation<br>Goes Here!</div>
    <div class="t-date" style="margin-top:26px">Friday, April 16, 2021</div>
  </div>
  <div class="copyright">© Copyright Halvora Trade Allies</div>
  <div class="brand-word" style="left:420px;top:270px">Halvora Trade Allies</div>
</div>

<div class="slide title-white" style="left:609px;top:810px">
  <div class="photo" role="img" aria-label="Light photo of a person in a white shirt working on a tablet" style="left:200px;top:0;width:363px;height:237px;background:linear-gradient(90deg,#ffffff 0%,#e8edf4 40%,#c9d3e0 100%)"></div>
  <div class="abs" style="left:52px;top:44px">
    <div class="t-big blue">Presentation Title<br>Goes Here!</div>
    <div class="t-sub" style="margin-top:10px">Subtitle of Presentation<br>Goes Here!</div>
    <div class="t-date" style="margin-top:26px">Friday, April 16, 2021</div>
  </div>
  <div class="abs" style="left:0;top:237px;width:563px;height:79px;background:var(--blue)"></div>
  <div class="copyright" style="color:#dce4f0">© Copyright Halvora Trade Allies</div>
  <div class="brand-word light" style="left:418px;top:270px">Halvora Trade Allies</div>
</div>

<!-- Row 2 -->
<div class="slide title-dark" style="left:28px;top:1145px">
  <div class="photo" role="img" aria-label="Dark photo of hands holding a tablet with a business report chart, warm light" style="left:0;top:0;width:563px;height:237px;background:linear-gradient(100deg,#000 0%,#111 35%,#4a3a32 70%,#8a6a52 100%)"></div>
  <div class="arc" style="left:420px;top:190px"></div>
  <div class="abs" style="left:52px;top:44px;color:#fff">
    <div class="t-big">Presentation Title<br>Goes Here!</div>
    <div class="t-sub" style="margin-top:10px">Subtitle of Presentation<br>Goes Here!</div>
    <div class="t-date" style="margin-top:26px">Thursday, April 15, 2021</div>
  </div>
  <div class="copyright">© Copyright Halvora Trade Allies</div>
  <div class="brand-word" style="left:420px;top:270px">Halvora Trade Allies</div>
</div>

<div class="slide about" style="left:609px;top:1145px">
  <div class="slide-title" style="top:26px">About Halvora Trade Allies</div>
  <div class="photo" role="img" aria-label="Photo of hands holding a tablet showing a business report" style="left:0;top:75px;width:563px;height:94px;background:linear-gradient(90deg,#b5763f 0%,#d8b28c 40%,#e9dccd 60%,#c49a72 100%)"></div>
  <div class="abs" style="left:0;top:169px;width:563px;height:22px;background:var(--bar-dark);color:#fff;font-size:11px;text-align:center;line-height:22px">Our passion is the key factor for customer success</div>
  <div class="abs" style="left:45px;top:210px;width:473px;font-size:8.5px;text-align:center;line-height:1.15;color:#333">Digital transformation is changing the way we live, what we do and how we communicate with each other as well as how we do our business and shopping.<br>The customers are better informed and more independent in their decisions. The digital transformation has created great possibilities in more channels than ever.</div>
  <div class="footer"><div class="lead"></div><div class="mark">HTA</div><div class="line"></div><div class="page">4</div></div>
</div>

<!-- Row 3 -->
<div class="slide steps" style="left:28px;top:1480px">
  <div class="photo" role="img" aria-label="Photo of a shopping cart on a desk, tinted deep blue" style="left:0;top:0;width:563px;height:148px;background:linear-gradient(110deg,#0b4a93 0%,#0d4c92 55%,#3a679f 100%)"></div>
  <div class="slide-title" style="top:28px;color:#fff">Digital development and transformation</div>
  <div class="abs" style="left:50px;top:63px;width:463px;font-size:7.6px;line-height:1.15;text-align:center;color:#fff">To get knowledge about how products, services and information can be consumed with digital concepts and solutions is more necessary than ever for companies. They need this to adapt to their customers wishes and requirements. It is essential to go from believing to knowing to implementing. Using the knowledge about digital development and concepts give companies the right background to invest in digital solutions. This creates competitiveness and new business opportunities in a global environment.</div>

  <div class="step" style="left:33px">
    <div class="dot" style="background:var(--blue)"><svg viewBox="0 0 24 24" width="24" height="24"><path d="M12 3a6 6 0 0 0-3.5 10.9V16h7v-2.1A6 6 0 0 0 12 3z" fill="#fff"/><rect x="9" y="17" width="6" height="2" fill="#fff"/><rect x="10" y="20" width="4" height="1.5" fill="#fff"/></svg></div>
    <div class="label blue">Our Passion</div>
    <div class="desc">Halvora Trade Allies´s passion is to understand and follow the digital transformation and development and to use this knowledge to help customers to gain competitiveness.</div>
  </div>
  <div class="step" style="left:158px">
    <div class="dot" style="background:var(--orange)"><svg viewBox="0 0 24 24" width="24" height="24"><path d="M5 19 15 9M9 5l10 10" stroke="#fff" stroke-width="2.4" stroke-linecap="round"/><circle cx="16.5" cy="7.5" r="3" fill="none" stroke="#fff" stroke-width="2"/></svg></div>
    <div class="label orange">Concept<br>Development</div>
    <div class="desc">Together with our customers we identify the business opportunities and challenges and develop concepts according to this. The concepts include proposed digital solutions and best praxis.</div>
  </div>
  <div class="step" style="left:284px">
    <div class="dot" style="background:var(--blue)"><svg viewBox="0 0 24 24" width="24" height="24"><rect x="3" y="4" width="18" height="12" rx="1" fill="none" stroke="#fff" stroke-width="2"/><rect x="10" y="16" width="4" height="3" fill="#fff"/><rect x="7" y="19" width="10" height="2" fill="#fff"/></svg></div>
    <div class="label blue">Concept<br>Implementation</div>
    <div class="desc">New concepts and solutions are very dependent on a good implementation plan to be successful. Together with the customer we work out the best set-up.</div>
  </div>
  <div class="step" style="left:410px">
    <div class="dot" style="background:var(--orange)"><svg viewBox="0 0 24 24" width="24" height="24"><rect x="4" y="15" width="4" height="5" fill="#fff"/><rect x="10" y="12" width="4" height="8" fill="#fff"/><rect x="16" y="9" width="4" height="11" fill="#fff"/><path d="M4 11 11 6l3 2 6-4" stroke="#fff" stroke-width="1.8" fill="none"/></svg></div>
    <div class="label orange">Analytics And<br>Evaluation</div>
    <div class="desc">Before, during and after concept development it is crucial to regularly do analytics and evaluation. The result of this will be used to improve and refine concept development and implementation.</div>
  </div>
  <div class="footer"><div class="lead"></div><div class="mark">HTA</div><div class="line"></div><div class="page">5</div></div>
</div>

<div class="slide focus" style="left:609px;top:1480px">
  <h2 style="left:31px;top:26px">Focus Areas</h2>
  <h3 style="left:31px;top:88px">We work with the following<br>in digital development</h3>
  <ul style="left:31px;top:143px">
    <li>Customer and user experience</li>
    <li>Systems and solutions in store</li>
    <li>Digital development &nbsp;and transformation</li>
    <li>Digitalization and technology</li>
  </ul>
  <div class="photo" role="img" aria-label="Photo of a small shopping cart beside a laptop and hands holding a card" style="left:289px;top:0;width:240px;height:257px;background:linear-gradient(150deg,#c8553a 0%,#e0b39a 35%,#c9cfd8 70%,#aab6c6 100%)"></div>
  <div class="footer"><div class="lead"></div><div class="mark">HTA</div><div class="line"></div><div class="page">6</div></div>
</div>

<!-- Row 4 -->
<div class="slide focus" style="left:28px;top:1815px">
  <div class="photo" role="img" aria-label="Photo of two business people pointing at charts on a tablet" style="left:32px;top:0;width:240px;height:257px;background:linear-gradient(160deg,#1f2a3a 0%,#5d6f88 40%,#b9c6d8 70%,#e7ebf1 100%)"></div>
  <h2 style="left:298px;top:26px">Focus Areas</h2>
  <h3 style="left:298px;top:80px">We work with the following<br>technologies</h3>
  <ul style="left:298px;top:132px;width:240px;line-height:1.6">
    <li>Digital Signage</li>
    <li>Sound solutions</li>
    <li>Queue management solutions</li>
    <li>People counter technology</li>
    <li>Visitor Analytics</li>
    <li>Digital real estate solutions</li>
    <li style="line-height:1.1">Media sales digital communication in store</li>
  </ul>
  <div class="footer"><div class="lead"></div><div class="mark">HTA</div><div class="line"></div><div class="page">7</div></div>
</div>

<div class="slide chart" style="left:609px;top:1815px">
  <div class="slide-title" style="top:26px"><span class="blue">Slide Title</span><span class="plain"> Goes Here!</span></div>
  <svg class="abs" style="left:40px;top:85px" width="290" height="165" viewBox="0 0 290 165" font-family="Montserrat,sans-serif">
    <g font-size="7" fill="#555" text-anchor="end">
      <text x="8" y="10">6</text><text x="8" y="33">5</text><text x="8" y="56">4</text><text x="8" y="79">3</text><text x="8" y="102">2</text><text x="8" y="125">1</text><text x="8" y="148">0</text>
    </g>
    <line x1="18" y1="146" x2="280" y2="146" stroke="#bbb" stroke-width="1"/>
    <g>
      <rect x="30" y="47" width="10" height="99" fill="#0b4a93"/><rect x="43" y="91" width="10" height="55" fill="#f08a1e"/><rect x="56" y="100" width="10" height="46" fill="#333"/>
      <rect x="93" y="88" width="10" height="58" fill="#0b4a93"/><rect x="106" y="45" width="10" height="101" fill="#f08a1e"/><rect x="119" y="100" width="10" height="46" fill="#333"/>
      <rect x="156" y="66" width="10" height="80" fill="#0b4a93"/><rect x="169" y="105" width="10" height="41" fill="#f08a1e"/><rect x="182" y="77" width="10" height="69" fill="#333"/>
      <rect x="219" y="43" width="10" height="103" fill="#0b4a93"/><rect x="232" y="82" width="10" height="64" fill="#f08a1e"/><rect x="245" y="31" width="10" height="115" fill="#333"/>
    </g>
    <g font-size="6.5" fill="#555" text-anchor="middle">
      <text x="48" y="157">Category 1</text><text x="111" y="157">Category 2</text><text x="174" y="157">Category 3</text><text x="237" y="157">Category 4</text>
    </g>
  </svg>
  <div class="legend" style="top:93px">
    <div class="item"><i style="background:var(--blue)"></i><b class="blue">Title Goes Here!</b><p>Lorem ipsum dolor sit amet, at laborum nibh duis mauris. Per ultrices lectus sed metus tristique eu. Diam suspendisse ac ipsum</p></div>
    <div class="item"><i style="background:var(--orange)"></i><b class="orange">Title Goes Here!</b><p>Lorem ipsum dolor sit amet, at laborum nibh duis mauris. Per ultrices lectus sed metus tristique eu. Diam suspendisse ac ipsum</p></div>
    <div class="item"><i style="background:#333"></i><b>Title Goes Here!</b><p>Lorem ipsum dolor sit amet, at laborum nibh duis mauris. Per ultrices lectus sed metus tristique eu. Diam suspendisse ac ipsum</p></div>
  </div>
  <div class="footer"><div class="lead"></div><div class="mark">HTA</div><div class="line"></div><div class="page">8</div></div>
</div>

<!-- Row 5 -->
<div class="slide table" style="left:28px;top:2150px">
  <div class="slide-title" style="top:26px"><span class="blue">Slide Title</span><span class="plain"> Goes Here!</span></div>
  <table class="data">
    <tr><th style="width:186px">Heading Goes Here!</th><th>Heading 1</th><th>Heading 2</th><th>Heading 3</th><th class="accent">Heading 4</th></tr>
    <tr><td>Lorem ipsum dolor sit amet ...</td><td>23</td><td>34</td><td>09</td><td>98</td></tr>
    <tr><td>Lorem ipsum dolor sit amet ...</td><td>44</td><td>89</td><td>12</td><td>78</td></tr>
    <tr><td>Lorem ipsum dolor sit amet ...</td><td>56</td><td>99</td><td>89</td><td>98</td></tr>
    <tr><td>Lorem ipsum dolor sit amet ...</td><td>78</td><td>88</td><td>56</td><td>88</td></tr>
  </table>
  <div class="footer"><div class="lead"></div><div class="mark">HTA</div><div class="line"></div><div class="page">9</div></div>
</div>

<div class="slide contact-slide" style="left:609px;top:2150px;background:#000">
  <div class="photo" role="img" aria-label="Street map of the office neighbourhood fading into black" style="left:0;top:0;width:563px;height:316px;background:linear-gradient(90deg,#000 0%,#0a0a0c 30%,#3a4150 60%,#8ea0b8 85%,#a9b8cb 100%)"></div>
  <div class="contact" style="left:46px;top:108px">
    <div class="mark">HTA</div>
    <h4>Contact Us</h4>
    <div class="addr">Ängsvägen 8,<br>234 41 LOMMA</div>
    <div style="margin-top:14px">
      <div class="row"><svg viewBox="0 0 24 24"><path d="M6 3h4l2 5-3 2a11 11 0 0 0 5 5l2-3 5 2v4a2 2 0 0 1-2 2A17 17 0 0 1 4 5a2 2 0 0 1 2-2z" fill="#fff"/></svg>+46-701234567</div>
      <div class="row"><svg viewBox="0 0 24 24"><circle cx="12" cy="12" r="4" fill="none" stroke="#fff" stroke-width="2.5"/><path d="M16 8v5a3 3 0 0 0 6 0v-1a10 10 0 1 0-4 8" fill="none" stroke="#fff" stroke-width="2.5"/></svg>info@halvoratradeallies.se</div>
      <div class="row"><svg viewBox="0 0 24 24"><circle cx="12" cy="12" r="9" fill="none" stroke="#fff" stroke-width="2"/><path d="M3 12h18M12 3c-4 5-4 13 0 18M12 3c4 5 4 13 0 18" fill="none" stroke="#fff" stroke-width="1.6"/></svg>https://halvoratradeallies.se</div>
    </div>
  </div>
</div>

<!-- Closing -->
<div class="slide thanks" style="left:319px;top:2485px;background:#000">
  <div class="photo" role="img" aria-label="Dark photo of a hand holding a phone with glowing app icons" style="left:0;top:0;width:563px;height:316px;background:radial-gradient(ellipse at 62% 45%,#5a4630 0%,#2a231c 30%,#0c0c0d 60%,#000 100%)"></div>
  <div class="abs" style="left:52px;top:55px;color:#fff">
    <div style="font-size:22px;font-weight:500">Thank You!</div>
    <div style="font-size:13px;margin-top:2px">for your attention and valuable time</div>
  </div>
  <div class="contact" style="left:46px;top:145px">
    <div class="mark">HTA</div>
    <h4>Contact Us</h4>
    <div style="margin-top:12px">
      <div class="row"><svg viewBox="0 0 24 24"><path d="M6 3h4l2 5-3 2a11 11 0 0 0 5 5l2-3 5 2v4a2 2 0 0 1-2 2A17 17 0 0 1 4 5a2 2 0 0 1 2-2z" fill="#fff"/></svg>+46-701234567</div>
      <div class="row"><svg viewBox="0 0 24 24"><circle cx="12" cy="12" r="4" fill="none" stroke="#fff" stroke-width="2.5"/><path d="M16 8v5a3 3 0 0 0 6 0v-1a10 10 0 1 0-4 8" fill="none" stroke="#fff" stroke-width="2.5"/></svg>info@halvoratradeallies.se</div>
      <div class="row"><svg viewBox="0 0 24 24"><circle cx="12" cy="12" r="9" fill="none" stroke="#fff" stroke-width="2"/><path d="M3 12h18M12 3c-4 5-4 13 0 18M12 3c4 5 4 13 0 18" fill="none" stroke="#fff" stroke-width="1.6"/></svg>https://halvoratradeallies.se</div>
    </div>
  </div>
  <div class="abs" style="left:0;top:300px;width:563px;text-align:center;font-size:5.5px;color:#444">© Copyright Halvora Trade Allies</div>
</div>

</body>
</html>
```